High End Business Card Design for Flooring Store

Looking for a new card design for our hardwood flooring company. We have no print budget for these and are open to cards made from wood, metal, cardstock with embossed print ... or any combination of these. No plastic.

We sell luxury products and I want the cards to reflect our image of quality and class.

Our contact information as such;
Employee Name
418 Colbrook Blvd.
Corvale, WQ
K9R-3M5
(555) 214-3968
Employee email @velkaflooring.com

Target Market(s)

Home Builders

Contact Information for Business Card

Emnployee name, business contact information

```html
<!DOCTYPE html>
<html lang="en">
<head>
<meta charset="utf-8">
<title>Velka Flooring – Business Card</title>
<link href="https://fonts.googleapis.com/css2?family=Montserrat:wght@400;500&family=Arimo:wght@400&display=swap" rel="stylesheet">
<style>
  :root {
    --backdrop: #353334;
    --paper: #ffffff;
    --brand-red: #922b26;
    --brand-gold: #e8b32a;
    --charcoal: #3e3e3e;
    --charcoal-light: #4a4a4c;
    --ink: #333333;
    --tagline: #666666;
    --on-dark: #ffffff;
  }
  * { margin: 0; padding: 0; box-sizing: border-box; }
  html, body { width: 1200px; height: 941px; overflow: hidden; }
  body { background: var(--backdrop); position: relative; font-family: "Arimo", Arial, sans-serif; }

  .card { position: absolute; top: 316px; width: 514px; height: 308px; background: var(--paper); overflow: hidden; }
  .card--front { left: 62px; }
  .card--back { left: 621px; }
  .card__graphics { position: absolute; inset: 0; }

  .brand { position: absolute; display: flex; align-items: center; }
  .brand__mark { background: var(--brand-gold); flex: none; }
  .brand__name { font-family: "Montserrat", sans-serif; font-weight: 500; color: var(--brand-red); line-height: 1; }
  .tagline { position: absolute; font-family: "Montserrat", sans-serif; color: var(--tagline); text-align: center; line-height: 1.1; transform: translateX(-50%); white-space: nowrap; }

  .card--front .brand { left: 8px; top: 12px; gap: 6px; }
  .card--front .brand__mark { width: 16px; height: 16px; }
  .card--front .brand__name { font-size: 33px; }
  .card--front .tagline { left: 88px; top: 46px; font-size: 9px; }

  .person { position: absolute; right: 50px; top: 78px; text-align: right; color: var(--ink); }
  .person__name { font-size: 33px; line-height: 1; letter-spacing: 0.2px; }
  .person__title { font-size: 19px; line-height: 1; margin-top: 3px; margin-right: 4px; }

  .contact { position: absolute; left: 33px; top: 178px; list-style: none; }
  .contact__item { display: flex; align-items: center; height: 28px; margin-bottom: 6px; color: var(--on-dark); font-size: 11.5px; line-height: 1.15; }
  .contact__icon { width: 28px; height: 28px; margin-right: 6px; flex: none; }

  .card--back .brand { left: 50%; top: 103px; transform: translateX(-50%); gap: 8px; }
  .card--back .brand__mark { width: 28px; height: 28px; }
  .card--back .brand__name { font-size: 50px; }
  .card--back .tagline { left: 261px; top: 156px; font-size: 13px; }
</style>
</head>
<body>

<section class="card card--front">
  <svg class="card__graphics" width="514" height="308" viewBox="0 0 514 308" aria-hidden="true">
    <polygon points="473,103 487,78 487,129" fill="var(--charcoal)"/>
    <polygon points="0,151 264,151 269,141 514,141 514,158 0,158" fill="var(--brand-red)"/>
    <rect x="0" y="158" width="514" height="150" fill="var(--charcoal-light)"/>
    <polygon points="0,158 260,158 295,233 260,308 0,308" fill="var(--charcoal)"/>
  </svg>

  <div class="brand">
    <span class="brand__mark"></span>
    <span class="brand__name">Velka</span>
  </div>
  <p class="tagline">Planchers &amp; Escaliers<br>Flooring &amp; Stairs</p>

  <div class="person">
    <p class="person__name">TOMAS REYLAND</p>
    <p class="person__title">Solution Manager</p>
  </div>

  <ul class="contact">
    <li class="contact__item">
      <svg class="contact__icon" viewBox="0 0 28 28" aria-hidden="true">
        <circle cx="14" cy="14" r="14" fill="var(--brand-red)"/>
        <path d="M6 12c0-3 4-4 8-4s8 1 8 4l-3 1-1-2h-8l-1 2z" fill="#fff"/>
        <path d="M9 14h10l2 6H7z" fill="#fff"/>
      </svg>
      <span>(555) 214-3968</span>
    </li>
    <li class="contact__item">
      <svg class="contact__icon" viewBox="0 0 28 28" aria-hidden="true">
        <circle cx="14" cy="14" r="14" fill="var(--brand-red)"/>
        <g fill="none" stroke="#fff" stroke-width="1.4">
          <circle cx="14" cy="14" r="8"/>
          <ellipse cx="14" cy="14" rx="3.5" ry="8"/>
          <path d="M6 14h16M7.5 10h13M7.5 18h13"/>
        </g>
      </svg>
      <span>Employee email @velkaflooring.com</span>
    </li>
    <li class="contact__item">
      <svg class="contact__icon" viewBox="0 0 28 28" aria-hidden="true">
        <circle cx="14" cy="14" r="14" fill="var(--brand-red)"/>
        <path d="M5 14l9-8 9 8" fill="none" stroke="#fff" stroke-width="2.4"/>
        <path d="M8 14l6-5 6 5v7h-4v-4h-4v4H8z" fill="#fff"/>
      </svg>
      <span>418 Colbrook Blvd.<br>Corvale, WQ. K9R-3M5</span>
    </li>
  </ul>
</section>

<section class="card card--back">
  <svg class="card__graphics" width="514" height="308" viewBox="0 0 514 308" aria-hidden="true">
    <polygon points="0,250 145,250 150,240 364,240 369,250 514,250 514,257 0,257" fill="var(--brand-red)"/>
    <rect x="0" y="257" width="514" height="51" fill="var(--charcoal)"/>
  </svg>

  <div class="brand">
    <span class="brand__mark"></span>
    <span class="brand__name">Velka</span>
  </div>
  <p class="tagline">Planchers &amp; Escaliers<br>Flooring &amp; Stairs</p>
</section>

</body>
</html>
```